Redesign business cards

We have a new logo and I am not that happy with the layout of our existing card and looking for a change. Font is a bit small and the green can be hard to read. Logo may need a tidy up as the copy I have is not that hi-res too so require you to produce a hi-res version of the logo for us too. There will be three individual business cards to produce with just the names and phone numbers being different. Address will change too, but use what you see on the card for now.

Industry/Entity Type

Business

Requirements
Nice to have
• You could consider a redesign to the new logo, just not too radical. We like the blue and green hexagons as we feel that they are representative of oil industry that we are in.

```html
<!DOCTYPE html>
<html lang="en">
<head>
<meta charset="utf-8">
<title>Vantora Oil Services – Business Card</title>
<link rel="stylesheet" href="https://fonts.googleapis.com/css2?family=Questrial&family=Michroma&display=swap">
<style>
  :root {
    --bg: #e4e4e2;
    --card: #ffffff;
    --green: #7cc242;
    --green-dark: #5e9a2c;
    --ink: #2f2f2f;
    --ink-soft: #555555;
    --rule: #b5b5b5;
  }
  * { margin: 0; padding: 0; box-sizing: border-box; }
  html, body {
    width: 1200px;
    height: 1057px;
    overflow: hidden;
    background: var(--bg);
  }
  .canvas {
    position: relative;
    width: 1200px;
    height: 1057px;
  }
  .business-card {
    position: absolute;
    left: 100px;
    top: 243px;
    width: 1000px;
    height: 571px;
    background: var(--card);
    box-shadow: 0 6px 24px rgba(0,0,0,0.12);
  }
  .brand {
    position: absolute;
    left: 64px;
    top: 40px;
    display: flex;
    align-items: center;
    gap: 18px;
  }
  .brand-mark {
    width: 44px;
    height: 44px;
    background: var(--green);
  }
  .brand-text { display: flex; flex-direction: column; }
  .brand-name {
    font-family: "Questrial", sans-serif;
    font-size: 62px;
    line-height: 1;
    color: var(--green);
  }
  .brand-tagline {
    font-family: "Questrial", sans-serif;
    font-size: 26px;
    line-height: 1.2;
    color: var(--green-dark);
  }
  .holder {
    position: absolute;
    left: 64px;
    top: 168px;
  }
  .holder-name {
    font-family: "Questrial", sans-serif;
    font-size: 40px;
    letter-spacing: 3px;
    color: var(--ink);
  }
  .holder-role {
    font-family: "Questrial", sans-serif;
    font-size: 14px;
    letter-spacing: 2px;
    color: var(--ink-soft);
    margin-top: 2px;
  }
  .contact-box {
    position: absolute;
    left: 64px;
    top: 262px;
    width: 872px;
    height: 268px;
    border: 2px solid var(--rule);
    border-radius: 34px;
    padding: 10px 40px 10px 28px;
  }
  .contact-row {
    display: flex;
    align-items: center;
    height: 62px;
    border-bottom: 1.5px solid var(--rule);
    margin-left: 62px;
  }
  .contact-row:last-child { border-bottom: none; }
  .contact-icon {
    width: 26px;
    height: 26px;
    margin-left: -62px;
    margin-right: 48px;
    border: 1.5px solid var(--rule);
    display: flex;
    align-items: center;
    justify-content: center;
    font-family: "Michroma", sans-serif;
    font-size: 11px;
    color: var(--green);
    box-shadow: 1px 1px 0 var(--rule);
  }
  .contact-value {
    font-family: "Michroma", sans-serif;
    font-size: 17px;
    letter-spacing: 1px;
    color: var(--ink);
    line-height: 1.35;
  }
</style>
</head>
<body>
<main class="canvas">
  <article class="business-card">
    <header class="brand">
      <div class="brand-mark"></div>
      <div class="brand-text">
        <span class="brand-name">Vantora</span>
        <span class="brand-tagline">Oil Services</span>
      </div>
    </header>

    <section class="holder">
      <h1 class="holder-name">DANIEL REYES</h1>
      <p class="holder-role">GENERAL MANAGER</p>
    </section>

    <section class="contact-box">
      <div class="contact-row">
        <span class="contact-icon">P</span>
        <span class="contact-value">012 555 0147</span>
      </div>
      <div class="contact-row">
        <span class="contact-icon">E</span>
        <span class="contact-value">info@vantora.com</span>
      </div>
      <div class="contact-row">
        <span class="contact-icon">W</span>
        <span class="contact-value">www.vantora-oil.com</span>
      </div>
      <div class="contact-row">
        <span class="contact-icon">A</span>
        <span class="contact-value">42 Harbour Road,<br>2nd building Street n.</span>
      </div>
    </section>
  </article>
</main>
</body>
</html>
```